Book Cover - Biography of Terrell and Joanne Whitfield

I am writing a biography about Terrell and Joanne Whitfield. I need a book cover designed for this. The title of the book is: Harvest of Courage: Terrell and Joanne Whitfield. I need one version for Ebook with size of 2000px wide by 3200px high and one version for audiobook with size of 3200px wide by 3200px high. *NOTE: Please only use non-copywrite images (open source / royalty-free.)

```html
<!DOCTYPE html>
<html lang="en">
<head>
<meta charset="utf-8">
<title>Harvest of Courage: Terrell and Joanne Whitfield — Book Cover</title>
<link rel="stylesheet" href="https://fonts.googleapis.com/css2?family=Cinzel:wght@400;700&display=swap">
<style>
  :root {
    --backdrop: #e6e6e6;
    --cover: #f7f7f7;
    --ink: #111111;
    --block: #000000;
    --photo-light: #b9b9b9;
    --photo-dark: #4a4a4a;
  }
  html, body {
    margin: 0;
    padding: 0;
    width: 1200px;
    height: 709px;
    overflow: hidden;
    background: var(--backdrop);
  }
  .canvas {
    position: relative;
    width: 1200px;
    height: 709px;
  }
  .cover {
    position: absolute;
    left: 400px;
    top: 34px;
    width: 400px;
    height: 640px;
    background: var(--cover);
    box-shadow: 0 6px 24px rgba(0, 0, 0, 0.12);
    font-family: "Cinzel", serif;
    color: var(--ink);
  }
  .cover-title {
    position: absolute;
    top: 50px;
    left: 0;
    right: 0;
    margin: 0;
    text-align: center;
    font-weight: 400;
    font-size: 15px;
    line-height: 1.3;
    letter-spacing: 0.02em;
  }
  .cover-title .strong {
    font-weight: 700;
    font-size: 18px;
  }
  .cover-title .line { display: block; }
  .portrait-grid {
    position: absolute;
    top: 160px;
    left: 38px;
    width: 324px;
    display: grid;
    grid-template-columns: 158px 158px;
    grid-template-rows: 181px 181px;
    gap: 8px;
  }
  .tile-solid { background: var(--block); }
  .tile-portrait {
    background: radial-gradient(circle at 50% 40%, var(--photo-dark) 0 30%, var(--photo-light) 75%);
  }
  .tile-portrait.darker {
    background: radial-gradient(circle at 50% 45%, #2e2e2e 0 32%, #7a7a7a 80%);
  }
  .cover-author {
    position: absolute;
    top: 562px;
    left: 0;
    right: 0;
    margin: 0;
    text-align: center;
    font-weight: 700;
    font-size: 11px;
    letter-spacing: 0.3em;
  }
</style>
</head>
<body>
  <div class="canvas">
    <main class="cover">
      <h1 class="cover-title">
        <span class="line"><span class="strong">Harvest</span> of <span class="strong">Courage:</span></span>
        <span class="line"><span class="strong">Terrell</span> and</span>
        <span class="line"><span class="strong">Joanne</span> <span class="strong">Whitfield</span></span>
      </h1>
      <div class="portrait-grid">
        <div class="tile-solid"></div>
        <div class="tile-portrait" role="img" aria-label="Black and white portrait photograph of Terrell Whitfield"></div>
        <div class="tile-portrait darker" role="img" aria-label="Black and white portrait photograph of Joanne Whitfield"></div>
        <div class="tile-solid"></div>
      </div>
      <p class="cover-author">Marian Holloway</p>
    </main>
  </div>
</body>
</html>
```